Birchwood Clover Business Cards

I need a business card with my logo, number, Facebook account, and some information about what I am selling. Green card with logo on the front. 555-218-3946 phone number, @birchwoodclover Facebook, •Orchardgrass Hay •Alfalfa Hay •Mixed Grass Hay , and “Premium Quality Hay” all written on the back.

Target Market(s)

Hay

Contact Information for Business Card

Phone number, Facebook, different types of hay.

Colors
00AB8E
00BBA5
67D7C9
C6EFE9
E9F9F6

```html
<!DOCTYPE html>
<html lang="en">
<head>
<meta charset="utf-8">
<title>Birchwood Clover Business Cards</title>
<link href="https://fonts.googleapis.com/css2?family=Arimo:wght@400;700&display=swap" rel="stylesheet">
<style>
  :root {
    --backdrop: #c4c4c4;
    --card-green: #00a651;
    --pattern-light: #1fd97f;
    --pattern-dark: #007a3b;
    --accent-green: #00a651;
    --ink: #1a1a1a;
    --divider: #b5b5b5;
    --card-white: #ffffff;
  }
  * { margin: 0; padding: 0; box-sizing: border-box; }
  html, body {
    width: 1200px; height: 800px; overflow: hidden;
    background: var(--backdrop);
    font-family: "Arimo", Arial, sans-serif;
  }
  .stage {
    position: relative; width: 1200px; height: 800px;
    display: flex; align-items: center; justify-content: center; gap: 50px;
  }
  .card {
    position: relative; width: 540px; height: 308px;
    border-radius: 18px; overflow: hidden;
  }

  /* Front */
  .card--front { background: var(--card-green); }
  .front-pattern {
    position: absolute; inset: 0;
    background: linear-gradient(135deg, var(--pattern-light) 0%, var(--card-green) 45%, var(--pattern-dark) 100%);
    opacity: 0.55;
  }
  .front-brand {
    position: absolute; left: 50%; top: 50%;
    transform: translate(-50%, -50%);
    display: flex; align-items: center; gap: 14px;
  }
  .front-brand__dot {
    width: 40px; height: 40px; border-radius: 50%; background: var(--card-white);
  }
  .front-brand__name {
    font-size: 30px; font-weight: 700; color: var(--ink); white-space: nowrap;
  }

  /* Back */
  .card--back { background: var(--card-white); border: 2px solid var(--accent-green); }
  .back-brand {
    position: absolute; left: 56px; top: 46px;
    display: flex; align-items: center; gap: 22px;
  }
  .back-brand__dot {
    width: 78px; height: 78px; border-radius: 50%; background: var(--accent-green);
  }
  .back-brand__rule { width: 1px; height: 80px; background: var(--divider); }
  .back-brand__name { font-size: 36px; font-weight: 700; color: var(--ink); white-space: nowrap; }

  .rule {
    position: absolute; left: 36px; right: 36px; height: 1.5px; background: var(--accent-green);
  }
  .rule--upper { top: 152px; }
  .rule--lower { top: 252px; }

  .contact {
    position: absolute; left: 36px; top: 168px; right: 36px;
  }
  .contact__head { display: flex; align-items: flex-end; gap: 10px; }
  .contact__name { font-size: 26px; font-weight: 700; color: var(--accent-green); line-height: 1; }
  .contact__role {
    font-size: 16px; color: var(--ink); padding-left: 10px;
    border-left: 1px solid var(--ink); line-height: 1.1;
  }
  .contact__lines { display: flex; gap: 34px; margin-top: 16px; }
  .contact__item { display: flex; align-items: center; gap: 8px; font-size: 17px; color: var(--ink); }
  .icon { width: 24px; height: 24px; flex: none; }
  .icon--plain { border-radius: 50%; background: var(--accent-green); }

  .products {
    position: absolute; left: 36px; right: 36px; top: 266px;
    display: flex; gap: 18px; list-style: none; font-size: 17px; color: var(--ink);
  }
  .products li { display: flex; align-items: center; gap: 7px; white-space: nowrap; }
  .products li::before {
    content: ""; width: 8px; height: 8px; border-radius: 50%; background: var(--accent-green);
  }
</style>
</head>
<body>
<main class="stage">
  <section class="card card--front" aria-label="Card front">
    <div class="front-pattern" role="img" aria-label="Repeating tonal pattern of the brand mark across the green card"></div>
    <div class="front-brand">
      <span class="front-brand__dot"></span>
      <span class="front-brand__name">Birchwood Clover</span>
    </div>
  </section>

  <section class="card card--back" aria-label="Card back">
    <div class="back-brand">
      <span class="back-brand__dot"></span>
      <span class="back-brand__rule"></span>
      <span class="back-brand__name">Birchwood Clover</span>
    </div>

    <div class="rule rule--upper"></div>

    <div class="contact">
      <div class="contact__head">
        <span class="contact__name">Jordan Mercer</span>
        <span class="contact__role">Owner</span>
      </div>
      <div class="contact__lines">
        <span class="contact__item">
          <svg class="icon" viewBox="0 0 24 24" aria-hidden="true">
            <circle cx="12" cy="12" r="12" fill="var(--accent-green)"/>
            <path d="M8.2 6.5l2 .3.9 2.6-1.3 1.1a7 7 0 0 0 3.7 3.7l1.1-1.3 2.6.9.3 2c-.6.9-1.6 1.4-2.7 1.2A9.5 9.5 0 0 1 7 9.2c-.2-1.1.3-2.1 1.2-2.7z" fill="#fff"/>
          </svg>
          555-218-3946
        </span>
        <span class="contact__item">
          <span class="icon icon--plain"></span>
          @birchwoodclover
        </span>
      </div>
    </div>

    <div class="rule rule--lower"></div>

    <ul class="products">
      <li>Orchardgrass Hay</li>
      <li>Alfalfa Hay</li>
      <li>Mixed Grass Hay</li>
    </ul>
  </section>
</main>
</body>
</html>
```